NZ's Most interesting purveyor of industrial furniture & exotic taxidermy needs a creative generic s

VELLA Heritage is seller of rustic industrial furniture, accessories, cowhides, antler chandeliers and taxidermy with two stores in Auckland, Ponsonby and Mt Eden. We need a luggage style swingtag which we would like to have on every piece of furniture and large item to add to the story of our brand. These tags will be generic and will not have any individual item information on them. The tags are to include the logo, our website and a small story about our brand. The inside card showing photo scenes of our industrial eclectic style. Specs and sizing of tag as attached. The overall design should exude an authentic, industrial vintage vibe.

Industry/Entity Type

Industrial

Requirements
Must have
• logo , images, website. Must have the insert card and layout as attached.

```html
<!DOCTYPE html>
<html lang="en">
<head>
<meta charset="utf-8">
<title>VELLA Heritage – Envelope Tag</title>
<link rel="stylesheet" href="https://fonts.googleapis.com/css2?family=Alegreya:ital,wght@0,400;0,700;1,400&display=swap">
<style>
  :root {
    --page: #ffffff;
    --page-edge: #dcdcdc;
    --paper-light: #f7e0a6;
    --paper-mid: #efcd8c;
    --paper-dark: #e2b476;
    --flap-light: #f8e6b8;
    --flap-dark: #ecd197;
    --tag-edge: #9a9a9a;
    --ink: #2a2520;
    --logo-ink: #3d3528;
    --brace: #9b8659;
    --ghost-name: rgba(196, 140, 72, 0.32);
    --caption: #8a8a8a;
  }
  html, body {
    margin: 0;
    padding: 0;
    background: var(--page);
    overflow: hidden;
  }
  .canvas {
    position: relative;
    width: 1200px;
    height: 810px;
    box-sizing: border-box;
    border: 1px solid var(--page-edge);
    background: var(--page);
    overflow: hidden;
    font-family: "Alegreya", Georgia, serif;
  }
  .tag-shapes {
    position: absolute;
    inset: 0;
  }
  .brand-name {
    position: absolute;
    left: 221px;
    width: 300px;
    top: 140px;
    margin: 0;
    text-align: center;
    font-weight: 700;
    font-size: 52px;
    line-height: 60px;
    letter-spacing: 1px;
    color: var(--logo-ink);
  }
  .brand-name span { display: block; }
  .brand-story {
    position: absolute;
    left: 570px;
    top: 117px;
    width: 200px;
    margin: 0;
    font-size: 15.5px;
    line-height: 21.8px;
    color: var(--ink);
  }
  .ghost-name {
    position: absolute;
    left: 221px;
    width: 612px;
    top: 520px;
    margin: 0;
    text-align: center;
    font-weight: 400;
    font-size: 84px;
    line-height: 100px;
    color: var(--ghost-name);
    white-space: nowrap;
  }
  .website {
    position: absolute;
    left: 221px;
    width: 612px;
    top: 626px;
    margin: 0;
    text-align: center;
    font-style: italic;
    font-size: 46px;
    line-height: 60px;
    letter-spacing: 0.5px;
    color: #000;
  }
  .caption {
    position: absolute;
    right: 200px;
    top: 764px;
    margin: 0;
    font-style: italic;
    font-size: 17px;
    letter-spacing: 0.5px;
    color: var(--caption);
  }
</style>
</head>
<body>
<main class="canvas">
  <svg class="tag-shapes" width="1200" height="810" viewBox="0 0 1200 810" aria-hidden="true">
    <defs>
      <radialGradient id="paper" cx="50%" cy="45%" r="70%">
        <stop offset="0" stop-color="var(--paper-light)"/>
        <stop offset="0.6" stop-color="var(--paper-mid)"/>
        <stop offset="1" stop-color="var(--paper-dark)"/>
      </radialGradient>
      <linearGradient id="flap" x1="0" y1="0" x2="1" y2="0">
        <stop offset="0" stop-color="var(--flap-dark)"/>
        <stop offset="0.5" stop-color="var(--flap-light)"/>
        <stop offset="1" stop-color="var(--flap-dark)"/>
      </linearGradient>
      <radialGradient id="stain" cx="50%" cy="50%" r="50%">
        <stop offset="0" stop-color="#c98a3c" stop-opacity="0.55"/>
        <stop offset="1" stop-color="#c98a3c" stop-opacity="0"/>
      </radialGradient>
    </defs>

    <g class="tag tag--front">
      <rect x="221" y="70" width="612" height="270" fill="url(#paper)" stroke="var(--tag-edge)" stroke-width="0.8"/>
      <polygon points="833,73 990,103 990,310 833,340" fill="url(#flap)" stroke="var(--tag-edge)" stroke-width="0.8"/>
      <circle cx="965" cy="302" r="14" fill="url(#stain)"/>
      <circle cx="236" cy="296" r="10" fill="url(#stain)" opacity="0.6"/>
      <path class="brace brace--open" d="M562 102 C540 104 539 118 539 145 L539 175 C539 190 533 197 520 199 C533 201 539 208 539 223 L539 255 C539 282 540 292 562 295" fill="none" stroke="var(--brace)" stroke-width="7" stroke-linecap="round" opacity="0.75"/>
      <path class="brace brace--close" d="M764 102 C786 104 787 118 787 145 L787 175 C787 190 793 197 806 199 C793 201 787 208 787 223 L787 255 C787 282 786 292 764 295" fill="none" stroke="var(--brace)" stroke-width="7" stroke-linecap="round" opacity="0.75"/>
    </g>

    <g class="tag tag--back">
      <rect x="221" y="447" width="612" height="268" fill="url(#paper)" stroke="var(--tag-edge)" stroke-width="0.8"/>
      <polygon points="833,450 990,482 990,687 833,715" fill="url(#flap)" stroke="var(--tag-edge)" stroke-width="0.8"/>
      <circle cx="963" cy="680" r="14" fill="url(#stain)"/>
      <circle cx="236" cy="672" r="10" fill="url(#stain)" opacity="0.6"/>
    </g>
  </svg>

  <h1 class="brand-name"><span>VELLA</span><span>Heritage</span></h1>

  <p class="brand-story">
    A unique store with<br>
    an eclectic aesthetic of<br>
    industrial and vintage<br>
    inspired pieces<br>
    modern and classic as<br>
    well as interesting and<br>
    unique accessories.
  </p>

  <p class="ghost-name" aria-hidden="true">VELLA Heritage</p>
  <p class="website">www.vellaheritage.com</p>

  <p class="caption">envelope tag</p>
</main>
</body>
</html>
```